Spa Brochure/service menu for existing spa for men and women

We need a brochure redesign to match our new logo, and business cards. Please keep in mind we love simplicity and no orchids. Tri-fold. unique. simple. eye catching front. Brochure serves as service menu in and out of business. Our clientel base is equal parts men and women. We are a privately owned and very unique business and would like our brochure to reflect that.

Target Market(s)

Men and women between 30- 65 from the greater NY area on a getaway in our quaint town

Industry/Entity Type

Business

Other font styles liked:
• Avalon. Anything that compliments current fonts in print and logo

Requirements
Must have
• Black, White and Gold design sticking with our new business cards (see attachement). Straight forward and clean. Our biggest concern is the front page being clean and appealing. (open to ideas) Logo on front page as main focus, design in background to highlight it a plus.
Nice to have
• Unique design. A simple map of our location in relation to Main Street and the ski slope on back page. Snail design featured.
Should not have
• No orchids. We hate orchids. No overly feminine tones. No generic spa images etc.

```html
<!DOCTYPE html>
<html lang="en">
<head>
<meta charset="utf-8">
<title>The Ashford Spa – Service Menu</title>
<link href="https://fonts.googleapis.com/css2?family=Mulish:ital,wght@0,400;0,600;0,700;1,700;1,800&display=swap" rel="stylesheet">
<style>
  :root {
    --ink: #231f20;
    --paper: #ffffff;
    --gold: #b39560;
    --gold-light: #d9c08a;
    --stage: #e9e6e1;
    --text-dark: #1c1a1a;
  }
  * { box-sizing: border-box; margin: 0; padding: 0; }
  html, body { width: 1200px; height: 943px; overflow: hidden; }
  body { background: var(--stage); font-family: "Mulish", Arial, sans-serif; position: relative; }

  .brochure {
    position: absolute; left: 35px; top: 36px; width: 1128px; height: 869px;
    background: var(--paper); box-shadow: 0 4px 14px rgba(0,0,0,.35); overflow: hidden;
  }
  .photo { position: absolute; }
  .photo--waxing { left: 0; top: 0; width: 753px; height: 322px;
    background: linear-gradient(120deg, #8e6f95 0%, #b592b8 35%, #e6d9d4 60%, #f4f1f0 100%); }
  .photo--face { left: 753px; top: 0; width: 375px; height: 432px;
    background: radial-gradient(circle at 45% 30%, #f6dccb 0%, #f1d0bd 30%, #f7f3f1 65%, #e9e2df 100%); }
  .photo--stones { left: 753px; top: 652px; width: 375px; height: 217px;
    background: linear-gradient(160deg, #ffffff 0%, #f2f2f2 40%, #9a9a9a 75%, #5b5b5b 100%); }

  .gold-rule { position: absolute; height: 10px;
    background: linear-gradient(90deg, var(--gold) 0%, var(--gold-light) 50%, var(--gold) 100%); }

  .menu-panel { position: absolute; left: 0; top: 322px; width: 375px; height: 547px;
    background: var(--ink); color: var(--paper); }
  .menu-panel h2 { text-align: center; font-style: italic; font-weight: 800; font-size: 19px; margin-top: 20px; }
  .wax-list { display: flex; gap: 30px; padding: 6px 0 0 18px; font-size: 12.5px; line-height: 17px; }
  .wax-list ul { list-style: none; width: 152px; }
  .wax-list li { display: flex; }
  .wax-list .dots { flex: 1; border-bottom: 1px dotted #bbb; margin: 0 2px 5px; }
  .wax-note { font-size: 12.5px; padding-left: 18px; line-height: 14px; }

  .packages { list-style: none; margin-top: 10px; }
  .packages li { text-align: center; font-style: italic; font-weight: 700; font-size: 16.5px;
    line-height: 21px; padding: 10px 10px; position: relative; }
  .packages li + li::before { content: ""; position: absolute; left: 20px; right: 20px; top: 0; height: 1px;
    background: linear-gradient(90deg, transparent, #8a7450, transparent); }

  .centre { position: absolute; left: 375px; top: 334px; width: 378px; height: 535px; text-align: center; }
  .map { position: absolute; left: 48px; top: 35px; width: 287px; height: 200px; border-radius: 22px;
    border: 4px solid #fff; box-shadow: 0 0 0 1px #cfcfcf, 0 2px 6px rgba(0,0,0,.25);
    background: linear-gradient(135deg, #e9e6df, #dedbd3); }

  .brand { font-weight: 400; color: var(--text-dark); letter-spacing: 2px; text-transform: uppercase; }
  .brand span { display: block; }
  .brand-tag { color: var(--text-dark); font-size: 11.5px; letter-spacing: .3px; }
  .centre .brand { position: absolute; left: 0; right: 0; top: 272px; font-size: 34px; line-height: 36px; }
  .centre .brand-tag { position: absolute; left: 0; right: 0; top: 382px; }

  .contact { position: absolute; left: 0; right: 0; top: 430px; color: var(--text-dark); font-size: 19px; line-height: 25px; font-style: normal; }
  .contact .call, .contact .mail { font-style: italic; font-weight: 700; }

  .logo-panel { position: absolute; left: 753px; top: 442px; width: 375px; height: 200px; background: var(--ink); text-align: center; }
  .logo-panel .brand { color: var(--paper); font-size: 42px; line-height: 44px; padding-top: 22px; }
  .logo-panel .brand-tag { color: var(--paper); font-size: 15px; margin-top: 6px; }
</style>
</head>
<body>
  <main class="brochure">
    <div class="photo photo--waxing" role="img" aria-label="Photo of a leg being waxed on a treatment table with a purple towel"></div>
    <div class="gold-rule" style="left:375px; top:322px; width:378px; height:12px;"></div>

    <div class="photo photo--face" role="img" aria-label="Photo of a relaxed spa guest in a towel holding red flowers above water"></div>
    <div class="gold-rule" style="left:753px; top:432px; width:375px;"></div>

    <section class="logo-panel">
      <p class="brand"><span>The</span><span>Ashford</span><span>Spa</span></p>
      <p class="brand-tag">a boutique spa for Men &amp; Women</p>
    </section>
    <div class="gold-rule" style="left:753px; top:642px; width:375px;"></div>

    <div class="photo photo--stones" role="img" aria-label="Photo of stacked black massage stones with green leaves"></div>

    <section class="menu-panel">
      <h2>Waxing</h2>
      <div class="wax-list">
        <ul>
          <li>Lips<span class="dots"></span>$10</li>
          <li>Chin<span class="dots"></span>$10</li>
          <li>Eyebrows<span class="dots"></span>$12</li>
          <li>Sideburns<span class="dots"></span>$10</li>
          <li>Lower Half Leg<span class="dots"></span>$25</li>
          <li>Upper Half Leg<span class="dots"></span>$40</li>
          <li>Full Leg<span class="dots"></span>$60</li>
          <li>Bikini<span class="dots"></span>$50</li>
        </ul>
        <ul>
          <li>Brazilian<span class="dots"></span>$65 &amp; up</li>
          <li>Chest<span class="dots"></span>$30 &amp; up</li>
          <li>Back<span class="dots"></span>$35 &amp; up</li>
          <li>Underarm<span class="dots"></span>$28</li>
          <li>Half Arm<span class="dots"></span>$18</li>
          <li>Full Arm<span class="dots"></span>$28</li>
          <li>Feet<span class="dots"></span>$10</li>
          <li>Hands<span class="dots"></span>$8</li>
        </ul>
      </div>
      <p class="wax-note">(top &amp; sides)</p>
      <ul class="packages">
        <li>Gift Certificates *map* with pi Packages</li>
        <li>Quiet Meadow</li>
        <li>Bright Skin Facial<br>55 Minute Swedish or Deep Tissue<br>Massage</li>
        <li>Brook Pebble</li>
        <li>Summit Calm</li>
        <li>A Hundred Petals</li>
        <li>The Apothecary</li>
      </ul>
    </section>

    <section class="centre">
      <div class="map" role="img" aria-label="Street map showing the spa location just off Main Street"></div>
      <p class="brand"><span>The</span><span>Ashford</span><span>Spa</span></p>
      <p class="brand-tag">a boutique spa for Men &amp; Women</p>
      <address class="contact">
        <div class="call">Call us : (555) 201 4836</div>
        <div class="mail">info@theashfordspa.com</div>
        <div>24 Larkspur Glen Road</div>
        <div>“Just off Main Street”</div>
      </address>
    </section>
  </main>
</body>
</html>
```